Logo for a Food & Beverage Franchise Company

We need a logo and stationary for a new company that just aquired a restaurant franchise. We need a sleep and professional logo with stationary.

Target Market(s)

Adults, resturaunt owners, franchisors (Companies who own food franchise companies such as Parvelli Head Office, Tollwick Grill International Franchise)
and Big Food and Beverage who wish to give franchise rights to us)

Industry/Entity Type

Restaurant

Logo Text

Velvet Harbor

Logo styles of interest
Emblem Logo
Pictorial/Combination Logo
Character Logo
Font styles to use
Serif
Sans Serif

Colors
ffc214
f78f20
f37022
faa54b
fece3e
fbed22

Requirements
Must have
• Maximum three color. The less the better.
Nice to have
• It does not have to have a crown, but if you wish to have a crown then it does not have to be so sharp and clear. Abstract is better.

```html
<!DOCTYPE html>
<html lang="en">
<head>
<meta charset="utf-8">
<title>Velvet Harbor — Identity Sheet</title>
<link rel="stylesheet" href="https://fonts.googleapis.com/css2?family=Cinzel:wght@400;500&family=Montserrat:wght@400;500&display=swap">
<style>
  :root {
    --wine: #7d0000;
    --wine-bright: #b5150c;
    --gold: #dca628;
    --gold-light: #f6cf2c;
    --gold-faint: #f3e0a8;
    --paper: #ffffff;
    --ink: #222222;
    --shadow: 0 3px 9px rgba(0,0,0,0.55);
    --serif: "Cinzel", "Times New Roman", serif;
    --sans: "Montserrat", Arial, sans-serif;
  }
  html, body { margin: 0; padding: 0; overflow: hidden; }
  body { width: 1200px; height: 1000px; background: var(--paper); position: relative; font-family: var(--sans); }

  .brand-name { font-family: var(--serif); color: var(--wine); font-weight: 400; margin: 0; white-space: nowrap; }
  .brand-dot { border-radius: 50%; background: var(--gold); }

  .hero-logo { position: absolute; left: 0; top: 40px; width: 1200px; text-align: center; }
  .hero-logo .brand-dot { width: 96px; height: 96px; margin: 70px auto 44px; }
  .hero-logo .brand-name { font-size: 52px; letter-spacing: 1px; }

  .sheet { position: absolute; background: var(--paper); box-shadow: var(--shadow); overflow: hidden; }
  .wave { position: absolute; left: 0; bottom: 0; width: 100%; height: 100%; }
  .red { fill: var(--wine); }
  .goldfill { fill: url(#goldSweep); }

  .mini-logo { position: absolute; text-align: center; }
  .mini-logo .brand-dot { margin: 0 auto 8px; }

  .letterhead { left: 110px; top: 385px; width: 400px; height: 567px; }
  .letterhead .mini-logo { left: 0; top: 22px; width: 400px; }
  .letterhead .mini-logo .brand-dot { width: 30px; height: 30px; }
  .letterhead .mini-logo .brand-name { font-size: 14px; }
  .letterhead .watermark { position: absolute; left: 115px; top: 200px; width: 170px; height: 170px; border-radius: 50%; background: var(--gold-faint); }
  .letterhead .contacts { position: absolute; right: 18px; bottom: 12px; color: #fff; font-size: 10px; text-align: right; line-height: 16px; }

  .contacts p { margin: 0; white-space: nowrap; }
  .contacts svg { width: 9px; height: 9px; vertical-align: -1px; margin-right: 4px; fill: currentColor; }

  .usb-drive { position: absolute; left: 542px; top: 418px; width: 208px; height: 65px; border-radius: 7px;
    background: linear-gradient(180deg, #e0321c 0%, var(--wine-bright) 45%, #8c0a04 100%); box-shadow: 0 2px 5px rgba(0,0,0,0.4); }
  .usb-drive .cap-line { position: absolute; left: 150px; top: 0; width: 2px; height: 65px; background: #3a0000; }
  .usb-drive .loop { position: absolute; left: 10px; top: 28px; width: 8px; height: 8px; border-radius: 50%; background: #6d0000; }
  .usb-drive .brand-dot { position: absolute; left: 62px; top: 14px; width: 36px; height: 36px; }

  .envelope { left: 540px; top: 530px; width: 460px; height: 200px; }
  .envelope .mini-logo { left: 18px; top: 14px; width: 90px; }
  .envelope .mini-logo .brand-dot { width: 28px; height: 28px; margin-bottom: 6px; }
  .envelope .mini-logo .brand-name { font-size: 11px; }
  .envelope .contacts { position: absolute; left: 22px; top: 68px; color: var(--wine); font-size: 8px; line-height: 13px; }

  .card-front { left: 537px; top: 765px; width: 273px; height: 165px; background: var(--wine); }
  .card-front .mini-logo { left: 0; top: 34px; width: 273px; }
  .card-front .brand-dot { width: 52px; height: 52px; margin-bottom: 12px; }
  .card-front .brand-name { color: #fff; font-size: 19px; }

  .card-back { left: 825px; top: 765px; width: 272px; height: 165px; }
  .card-back .mini-logo { left: 12px; top: 38px; width: 102px; }
  .card-back .mini-logo .brand-dot { width: 34px; height: 34px; }
  .card-back .mini-logo .brand-name { font-size: 11px; }
  .card-back .person { position: absolute; left: 134px; top: 22px; }
  .card-back .person-name { font-family: var(--serif); font-size: 15px; color: var(--ink); margin: 0; }
  .card-back .person-title { font-family: var(--sans); font-size: 12px; color: var(--wine); margin: 2px 0 6px; }
  .card-back .contacts { color: var(--ink); font-size: 8px; line-height: 17px; }
</style>
</head>
<body>
  <svg width="0" height="0" style="position:absolute">
    <defs>
      <linearGradient id="goldSweep" x1="0" y1="0" x2="1" y2="0">
        <stop offset="0" stop-color="#d8a023"/>
        <stop offset="0.4" stop-color="#f8d21a"/>
        <stop offset="1" stop-color="#f3d98a"/>
      </linearGradient>
      <symbol id="i-home" viewBox="0 0 10 10"><path d="M5 1 L10 5 H8.5 V9.5 H1.5 V5 H0 Z"/></symbol>
      <symbol id="i-phone" viewBox="0 0 10 10"><path d="M2.5 0 H7.5 V10 H2.5 Z M3.5 1 V8 H6.5 V1 Z"/></symbol>
      <symbol id="i-mail" viewBox="0 0 10 10"><path d="M0 2 H10 V8 H0 Z M0.8 2.6 L5 5.6 L9.2 2.6 Z" fill-rule="evenodd"/></symbol>
      <symbol id="i-globe" viewBox="0 0 10 10"><path d="M5 0 A5 5 0 1 0 5.01 0 Z M5 1 A4 4 0 1 1 4.99 1 Z M4.5 1 H5.5 V9 H4.5 Z M1 4.5 H9 V5.5 H1 Z" fill-rule="evenodd"/></symbol>
    </defs>
  </svg>

  <header class="hero-logo">
    <div class="brand-dot"></div>
    <h1 class="brand-name">Velvet Harbor</h1>
  </header>

  <section class="sheet letterhead">
    <div class="mini-logo"><div class="brand-dot"></div><p class="brand-name">Velvet Harbor</p></div>
    <div class="watermark"></div>
    <svg class="wave" viewBox="0 0 400 567" preserveAspectRatio="none">
      <path class="red" d="M0,548 C150,575 260,520 400,455 V567 H0 Z"/>
      <path class="goldfill" d="M0,480 C80,520 150,535 220,532 C170,540 80,545 0,540 Z"/>
    </svg>
    <div class="contacts">
      <p><svg><use href="#i-home"/></svg>Street 111</p>
      <p><svg><use href="#i-phone"/></svg>999 888 777</p>
      <p><svg><use href="#i-mail"/></svg>name@vh.org</p>
      <p><svg><use href="#i-globe"/></svg>velvetharbor.com</p>
    </div>
  </section>

  <div class="usb-drive">
    <div class="loop"></div>
    <div class="brand-dot"></div>
    <div class="cap-line"></div>
  </div>

  <section class="sheet envelope">
    <div class="mini-logo"><div class="brand-dot"></div><p class="brand-name">Velvet Harbor</p></div>
    <div class="contacts">
      <p><svg><use href="#i-home"/></svg>Street 111</p>
      <p><svg><use href="#i-phone"/></svg>999 888 777</p>
      <p><svg><use href="#i-mail"/></svg>name@vh.org</p>
      <p><svg><use href="#i-globe"/></svg>velvetharbor.com</p>
    </div>
    <svg class="wave" viewBox="0 0 460 200" preserveAspectRatio="none">
      <path class="red" d="M0,192 C180,205 300,160 460,135 V200 H0 Z"/>
      <path class="goldfill" d="M0,150 C60,180 150,185 250,180 C150,190 60,190 0,188 Z"/>
    </svg>
  </section>

  <section class="sheet card-front">
    <div class="mini-logo"><div class="brand-dot"></div><p class="brand-name">Velvet Harbor</p></div>
  </section>

  <section class="sheet card-back">
    <div class="mini-logo"><div class="brand-dot"></div><p class="brand-name">Velvet Harbor</p></div>
    <div class="person">
      <p class="person-name">Name Surname</p>
      <p class="person-title">Title</p>
      <div class="contacts">
        <p><svg><use href="#i-home"/></svg>Street 111</p>
        <p><svg><use href="#i-phone"/></svg>999 888 777</p>
        <p><svg><use href="#i-globe"/></svg>velvetharbor.com</p>
        <p><svg><use href="#i-mail"/></svg>name@vh.org</p>
      </div>
    </div>
    <svg class="wave" viewBox="0 0 272 165" preserveAspectRatio="none">
      <path class="red" d="M0,160 C110,165 200,150 272,125 V165 H0 Z"/>
      <path class="goldfill" d="M0,130 C40,150 90,152 150,150 C90,156 40,158 0,156 Z"/>
    </svg>
  </section>
</body>
</html>
```